We need your help in designing the graphical look of the home page of our web site: Plimora.com.

Plimora is an FREE online service that brings consumers and service providers together through online reservations.

Our service is in fact a web application (similar to quindle planner), so we will be using forms, widgets, menus and standard web controls (buttons, fields, links, etc). We need a design that will be easy to integrate with our programming.

This design project is for the HOME page, but we will choose the designer that will design the web page in photoshop in layers, so we can easily derive our other secondary pages ourselves.

If you have any questions please send us a message and we will gladly update the brief with a response.

Happy Designing!
Updates

Hi all, the menu on the home page should be something standard, like: Pricing, features, how it works.

once a user is logged in, they will see their toolbox at all times:
- My Box (links to their main page of bookings)
- My Faborites (view favorite businesses and book quickly with them)
- Settings (set parameters of their account)

There should be a My Profile page as well. 

Thanks!

Reason: I have extended the deadline to receive more designs.

Hi All,

UPDATE: we changed our vision of the home page to have a much simpler design.  something along the lines of chatterloom peeplark and crew lattice.

HOME PAGE:
light colors with white background.  simple, simple, simple!

header should not be big, logo, change language link. try with search bar (what and where).

body should be simple, with an image + register form only.

footer with links to pages for more info:
- Privacy,
- Getting started
- How it works
- Contact us
- FAQ
- Pricing

LOGGED IN PAGE:
when logged in, the header can be the same or reduced to maximize the "working area" (body).
body can be a 2 or 3 column design, as we have a main working area.  in your design, show a calendar.  we need a toolbar (side or top) that will have these buttons, links: MyBox, My Favorites, Settings, My Profile.
We need a section that will display latest messages or notifications.
keep the footer with the links.

Thank you all.

Reason: Holidays

Reason: holidays... lets spend time with our families!

Target Market(s)

Young and mobile consumers + professionals, businesses, restaurants and commerces wishing to offer online reservations (appointments and reservations)

Industry/Entity Type

Quindle

Requirements
Must have
• - Easy to integrate with web programming
- light weight visual design. We want something with light tone colors as background
- home page will have a content slider that will show some catch phrases.
- Overall design should be more on the "cartoony" side. Should give a casual, humour and friendly ambiance.

The home page should have these sections:
- a search section for consumers to find local businesses. They will search by specifying "What?" & "Where?"
- a content slider that will cycle through catch phrases and features. Each pane should have an image representative of the text.
- have 4 highlighted sections
- Plimora is great for (list of different businesses types that use plimora)
- Plimora is available for FREE to everyone
- Main features list (accept 24/7 reservations, never reveal your schedule, automatic reminders, marketing campaigns)
- The more you plim, the more you save! (info on our loyalty program that entitles consumers to greater savings and benefits).

One a user logs in, all the certer page info will be replaced by a content div that will allow content to display based on selected menu item
- My Box (opens the main section where all happens. This section should have a design that gives the impression that we're looking in a box)
- My Profile
- My Favorites
Should not have
• - Don't use actual photos of real people, rather opt for sketches and cartoony characters.

```html
<!DOCTYPE html>
<html lang="en">
<head>
<meta charset="utf-8">
<title>Plimora — Home</title>
<link rel="stylesheet" href="https://fonts.googleapis.com/css2?family=Marcellus+SC&family=Kristi&display=swap">
<style>
  :root {
    --teal-deep: #0b4350;
    --teal-ink: #0d4855;
    --teal-bright: #1eaac6;
    --teal-mid: #12889f;
    --teal-dark: #0c5f72;
    --page-light: #e9eaeb;
    --page-white: #ffffff;
    --muted: #8a8f92;
    --text-light: #ffffff;
  }
  * { margin: 0; padding: 0; box-sizing: border-box; }
  html, body { width: 1200px; height: 900px; overflow: hidden; }
  body { background: var(--page-light); }
  .canvas {
    position: relative;
    width: 1024px;
    height: 768px;
    transform: scale(1.171875);
    transform-origin: 0 0;
    background: linear-gradient(to bottom, var(--page-light) 0px, var(--page-white) 220px, var(--page-white) 300px, var(--page-light) 636px);
    font-family: "Marcellus SC", serif;
    color: var(--teal-ink);
    overflow: hidden;
  }
  .brand {
    position: absolute; left: 100px; top: 172px;
    display: flex; align-items: center; gap: 8px;
  }
  .brand-mark { width: 18px; height: 18px; background: var(--teal-mid); }
  .brand-name { font-size: 21px; letter-spacing: 1px; color: var(--teal-ink); }

  .field {
    position: absolute;
    background: var(--teal-deep);
    border-radius: 4px;
    color: var(--text-light);
    font-size: 13px;
    letter-spacing: 1.5px;
    display: flex; align-items: center;
  }
  .field-small { height: 30px; width: 240px; top: 98px; padding-left: 18px; }
  .field-large { left: 574px; width: 350px; height: 50px; padding-left: 20px; }

  .button {
    position: absolute;
    background: linear-gradient(to bottom, var(--teal-bright), var(--teal-dark));
    border: 1px solid var(--teal-deep);
    border-radius: 4px;
    color: var(--text-light);
    letter-spacing: 3px;
    display: flex; align-items: center; justify-content: center;
  }
  .button-signin { left: 824px; top: 98px; width: 100px; height: 30px; font-size: 13px; }
  .button-signup { left: 574px; top: 500px; width: 150px; height: 50px; font-size: 15px; letter-spacing: 4px; }

  .remember { position: absolute; left: 303px; top: 137px; display: flex; align-items: center; gap: 5px; font-size: 10px; letter-spacing: 1px; }
  .checkbox { width: 13px; height: 13px; border: 2px solid var(--teal-deep); border-radius: 3px; }
  .forgot { position: absolute; left: 564px; top: 138px; font-size: 10px; letter-spacing: 1px; }

  .join-heading { position: absolute; left: 575px; top: 242px; font-size: 17px; letter-spacing: 2px; font-weight: 700; }
  .join-note { position: absolute; left: 776px; top: 250px; font-family: "Kristi", cursive; font-size: 23px; color: var(--muted); }

  .tagline { position: absolute; left: 98px; top: 290px; font-family: "Kristi", cursive; color: var(--teal-ink); font-size: 44px; line-height: 70px; }
  .tagline span { display: block; }
  .tagline .second { padding-left: 37px; }
  .tagline big { font-size: 62px; }

  .footer-links {
    position: absolute; left: 0; top: 637px; width: 1024px; height: 101px;
    background: linear-gradient(to bottom, var(--teal-bright), var(--teal-dark));
    border-top: 2px solid #8fd3e1;
  }
  .link-list { position: absolute; top: 14px; list-style: none; }
  .link-list li { height: 30px; font-size: 11.5px; letter-spacing: 1.5px; color: var(--text-light); padding-left: 21px; position: relative; }
  .link-list li::before { content: ""; position: absolute; left: 0; top: 5px; width: 4px; height: 4px; border-radius: 50%; background: var(--text-light); }
  .col-1 { left: 110px; } .col-2 { left: 424px; } .col-3 { left: 780px; }

  .copyright { position: absolute; right: 16px; top: 748px; font-size: 10px; letter-spacing: 2px; color: var(--teal-deep); }
</style>
</head>
<body>
<div class="canvas">
  <header>
    <div class="brand"><span class="brand-mark"></span><span class="brand-name">Plimora</span></div>
    <div class="field field-small" style="left:304px">Email</div>
    <div class="field field-small" style="left:564px">Password</div>
    <div class="button button-signin">Sign In</div>
    <div class="remember"><span class="checkbox"></span>Remember Me</div>
    <div class="forgot">Forgot your Password?</div>
  </header>

  <main>
    <p class="tagline"><span>The More You <big>Plim,</big></span><span class="second">The More You <big>Save!</big></span></p>
    <h2 class="join-heading">New to Plimora?</h2>
    <p class="join-note">Join Today It's Free!</p>
    <div class="field field-large" style="top:290px">Full Name</div>
    <div class="field field-large" style="top:360px">email</div>
    <div class="field field-large" style="top:430px">Password</div>
    <div class="button button-signup">Sign Up</div>
  </main>

  <footer>
    <nav class="footer-links">
      <ul class="link-list col-1"><li>Overview</li><li>Features</li><li>FAQ’s</li></ul>
      <ul class="link-list col-2"><li>Getting started</li><li>Loyalty Scheme</li><li>About Plimora</li></ul>
      <ul class="link-list col-3"><li>Contact Us</li><li>Privacy</li><li>Terms of Service</li></ul>
    </nav>
    <p class="copyright">Copyright 2011, Plimora</p>
  </footer>
</div>
</body>
</html>
```